card design for engineering consultancy

engineering drafting and project management company the provides drafting services for.
Electrical, Hydraulic, Mechanical, and Civil services
The company is called Q7R Services and logo is as attached
Information on card should be.
1. Logo
2.website : Q7RServices.example
3. email : info@Q7RServices.example
4. Phone: (+61) 400512836
5. Motto: Design - Document - Develop - Deliver

this card should be basically used for business identification only

Target Market(s)

electricians plumbers air conditioning installers and civil contractors

Industry/Entity Type

engineering, drafting, electrical, plumbing, airconditioning, civil

Contact Information for Business Card

1. Logo 2.website : Q7RServices.example 3. email : info@Q7RServices.example 4. Phone: (+61) 400512836 5. Motto: Design - Document - Develop - Deliver

Font styles to use
Serif

Requirements
Must have
• logo
Nice to have
• something inovative and different that makes it stand out from being just another business card

```html
<!DOCTYPE html>
<html lang="en">
<head>
<meta charset="utf-8">
<title>Q7R Services – Business Card</title>
<link rel="stylesheet" href="https://fonts.googleapis.com/css2?family=Josefin+Sans:wght@300;400;600&display=swap">
<style>
  :root {
    --backdrop: #1b1b1b;
    --card-face: #0e0e0e;
    --card-pattern: #151515;
    --brand-red: #d11a27;
    --brand-grey: #5a5655;
    --text-light: #b9b7b6;
    --rule: #5c5c5c;
  }
  * { box-sizing: border-box; margin: 0; padding: 0; }
  html, body { width: 1200px; height: 1015px; overflow: hidden; }
  body {
    background: radial-gradient(ellipse at 50% 45%, #2a2a2a 0%, var(--backdrop) 70%);
    font-family: "Josefin Sans", sans-serif;
    display: flex;
    flex-direction: column;
    align-items: center;
    justify-content: center;
    gap: 44px;
  }
  .card {
    width: 760px;
    height: 434px;
    border: 13px solid var(--brand-red);
    background: var(--card-face);
    position: relative;
    box-shadow: 0 18px 40px rgba(0,0,0,.55);
  }
  .card-front .pattern-field {
    position: absolute;
    inset: 0;
    background: var(--card-pattern);
  }
  .brand-name {
    font-family: "Josefin Sans", sans-serif;
    font-weight: 600;
    color: var(--brand-grey);
    text-transform: uppercase;
    letter-spacing: .12em;
    white-space: nowrap;
  }
  .card-front .brand-name {
    position: absolute;
    top: 50%;
    left: 50%;
    transform: translate(-50%, -50%);
    font-size: 64px;
  }
  .card-back { display: flex; flex-direction: column; align-items: center; }
  .card-back .brand-name {
    margin-top: 86px;
    font-size: 46px;
  }
  .motto {
    margin-top: 58px;
    color: var(--brand-red);
    font-weight: 400;
    font-size: 27px;
    letter-spacing: .42em;
    white-space: nowrap;
  }
  .divider {
    width: 600px;
    height: 1px;
    background: var(--rule);
    margin-top: 14px;
  }
  .contact-row {
    margin-top: 18px;
    display: flex;
    gap: 42px;
    list-style: none;
    color: var(--text-light);
    font-weight: 300;
    font-size: 15px;
    letter-spacing: .04em;
  }
  .contact-row li { display: flex; align-items: center; gap: 8px; }
  .contact-icon { width: 15px; height: 15px; fill: none; stroke: var(--brand-red); stroke-width: 1.6; }
  .contact-icon.solid { fill: var(--brand-red); stroke: none; }
</style>
</head>
<body>
  <section class="card card-front" aria-label="Card front">
    <div class="pattern-field" role="img" aria-label="Subtle repeating brand pattern across the card background"></div>
    <h1 class="brand-name">Q7R Services</h1>
  </section>

  <section class="card card-back" aria-label="Card back">
    <h2 class="brand-name">Q7R Services</h2>
    <p class="motto">Document - Develop - Deliver</p>
    <div class="divider"></div>
    <ul class="contact-row">
      <li>
        <svg class="contact-icon solid" viewBox="0 0 24 24" aria-hidden="true"><path d="M6.6 10.8a15.1 15.1 0 0 0 6.6 6.6l2.2-2.2a1 1 0 0 1 1-.25 11.4 11.4 0 0 0 3.6.57 1 1 0 0 1 1 1V20a1 1 0 0 1-1 1A17 17 0 0 1 3 4a1 1 0 0 1 1-1h3.5a1 1 0 0 1 1 1c0 1.25.2 2.45.57 3.57a1 1 0 0 1-.25 1z"/></svg>
        <span>(+61) 400512836</span>
      </li>
      <li>
        <svg class="contact-icon" viewBox="0 0 24 24" aria-hidden="true"><rect x="2.5" y="5" width="19" height="14" rx="1"/><path d="M2.5 5.5 12 13l9.5-7.5"/></svg>
        <span>info@Q7RServices.example</span>
      </li>
      <li>
        <svg class="contact-icon" viewBox="0 0 24 24" aria-hidden="true"><circle cx="12" cy="12" r="9.5"/><ellipse cx="12" cy="12" rx="4.2" ry="9.5"/><path d="M2.5 12h19M4 7h16M4 17h16"/></svg>
        <span>Q7RServices.example</span>
      </li>
    </ul>
  </section>
</body>
</html>
```